Flyer needed For the Council for Stewardship of Public Works

With an increasing need for professional staffing in our design and construction industry it is important for organizations to be able to attract, support, and retain people of all genders. With the increase of women entering the design/construction industry, we need to be able to identify and address the specific needs of women in our industry, including those A/E’s who are on the facility Owner side.

This Forum will provide a venue to openly discuss the issues affecting our industry and ideas to address those issues.The program includes time for presentations and a panel discussion by accomplished women in our industry, and facilitated table and open discussions to form solutions with your peers. You will come away with ideas you can implement within your organization to build processes and a supportive culture for women

IN THE ATTACHMENTS
* you'll find our company logo

Target Market(s)

Women in the design and construction industry

Industry/Entity Type

Construction

Requirements
Must have
• Logo, event name, date, time, location, panelists names and pics, NBF continuing education provided, contact information: Maren Holtzclaw, maren.holtzclaw@c-sfpw.org, (555) 740-1938
• Register at: www.c-sfpw.org/events
• Design should encompass the description given above.
Nice to have
• Colors that compliment our logo

```html
<!DOCTYPE html>
<html lang="en">
<head>
<meta charset="utf-8">
<title>A&amp;E Industry Women's Mini-Forum &amp; Workshop</title>
<link href="https://fonts.googleapis.com/css2?family=Open+Sans:wght@400;600;700;800&family=Oswald:wght@500;600&display=swap" rel="stylesheet">
<style>
  :root {
    --blue: #1d3f93;
    --blue-dark: #142d6e;
    --green: #8cc63f;
    --green-dark: #6fa82a;
    --ink: #2b2b2b;
    --paper: #ffffff;
    --stage: #e9ebee;
  }
  * { box-sizing: border-box; margin: 0; padding: 0; }
  html, body { width: 900px; height: 1200px; overflow: hidden; background: var(--stage); }
  .flyer {
    position: relative; width: 900px; height: 1200px; background: var(--paper);
    font-family: "Open Sans", Arial, sans-serif; color: var(--ink);
  }
  .header { position: absolute; top: 0; left: 0; width: 900px; height: 150px; background: var(--paper); }
  .brand { position: absolute; right: 48px; top: 34px; text-align: left; }
  .brand-name { display: flex; align-items: center; gap: 12px; font-weight: 800; font-size: 54px; color: var(--blue); line-height: 1; }
  .brand-mark { width: 22px; height: 22px; background: var(--green); border-radius: 50%; }
  .brand-tag { margin-top: 8px; font-size: 14px; color: var(--blue); font-weight: 600; padding-left: 34px; }
  .hero {
    position: absolute; top: 150px; left: 0; width: 900px; height: 420px;
    background: linear-gradient(180deg, #3f7fc4 0%, #8fb6dc 45%, #e8c79a 72%, #5d4a3a 100%);
  }
  .title-banner {
    position: absolute; top: 468px; left: 0; width: 560px; padding: 16px 26px 18px 40px;
    background: var(--green); color: #fff;
    font-family: "Oswald", "Arial Narrow", sans-serif; font-weight: 600; font-size: 24px; line-height: 1.3;
    text-transform: uppercase;
  }
  .title-banner .date { color: #fff79a; }
  .intro { position: absolute; top: 598px; left: 48px; width: 804px; font-size: 13px; line-height: 1.55; }
  .intro p + p { margin-top: 10px; }
  .intro .highlight { color: var(--green-dark); font-weight: 600; }
  .program {
    position: absolute; top: 808px; left: 160px; width: 560px;
    border: 3px solid var(--blue); padding: 10px 24px 12px; text-align: center;
  }
  .program h2 { font-size: 21px; line-height: 1.3; font-weight: 700; color: var(--blue); margin-bottom: 4px; }
  .program .lead { font-weight: 700; font-size: 14.5px; color: var(--blue); line-height: 1.35; }
  .program ul { list-style: none; margin-top: 5px; font-size: 12.5px; line-height: 1.42; }
  .partner-badge { position: absolute; top: 970px; left: 752px; width: 80px; height: 80px; border: 3px solid var(--blue); background: #f2f5fb; }
  .footer-rule { position: absolute; top: 1082px; left: 0; width: 900px; height: 8px; background: var(--green); }
  .footer {
    position: absolute; top: 1090px; left: 0; width: 900px; height: 110px; background: var(--blue);
    color: #fff; text-align: center; padding-top: 16px;
  }
  .footer .phone { display: flex; align-items: center; justify-content: center; gap: 12px; font-size: 34px; font-weight: 800; line-height: 1.2; }
  .footer .register { margin-top: 6px; font-size: 22px; font-weight: 700; letter-spacing: .5px; }
  .footer .register span { color: var(--green); }
</style>
</head>
<body>
<div class="flyer">
  <header class="header">
    <div class="brand">
      <div class="brand-name"><span class="brand-mark"></span>C-SfPW</div>
      <div class="brand-tag">Council for Stewardship of Public Works</div>
    </div>
  </header>

  <div class="hero" role="img" aria-label="Photograph of an industrial plant skyline with smokestacks under a blue sky at sunset"></div>

  <div class="title-banner">
    A&amp;E Industry Women's Mini-Forum &amp;<br>
    Workshop – <span class="date">January 16, 2019</span><br>
    Harborline Suites, San Marcos, Texas
  </div>

  <section class="intro">
    <p>With an increasing need for professional staffing in our design and construction industry it is important for organizations to be able to attract, support, and retain people of all genders. With the increase of women entering the design/construction industry, we need to be able to identify and address the specific needs of women in our industry, including those A/E's who are on the facility Owner side. This Forum will provide a venue to openly discuss the issues affecting our industry and ideas to address those issues.</p>
    <p>The program includes time for presentations and a panel discussion by accomplished women in our industry, and facilitated table and open discussions to form solutions with your peers. <span class="highlight">You will come away with ideas you can implement within your organization to build processes and a supportive culture for women.</span></p>
    <p>A visual note-taker and separate scribe will be utilized to compile ideas and solutions, for distribution to participants after the event.</p>
  </section>

  <section class="program">
    <h2>Program Timing:</h2>
    <div class="lead">1:00, Registration and Networking (refreshments)<br>1:30, Program</div>
    <ul>
      <li>1:35, Welcome and introduce panel moderator (Dana Ellery)</li>
      <li>1:40, Presentations</li>
      <li>2:30, Panel/Q&amp;A</li>
      <li>3:20, Break (refreshments)</li>
      <li>3:40, Table discussions – facilitated; focus on ideas to address issues</li>
      <li>4:10, Report out and open discussion – solutions!</li>
      <li>4:40, Conclusions, Closing</li>
      <li>4:45, Adjourn</li>
    </ul>
  </section>

  <div class="partner-badge" aria-label="NBF continuing education badge"></div>

  <div class="footer-rule"></div>
  <footer class="footer">
    <div class="phone">
      <svg width="30" height="30" viewBox="0 0 24 24" aria-hidden="true"><path fill="#fff" d="M6.6 10.8a15.1 15.1 0 0 0 6.6 6.6l2.2-2.2c.3-.3.7-.4 1-.2 1.1.4 2.3.6 3.6.6.6 0 1 .4 1 1V20c0 .6-.4 1-1 1C10.6 21 3 13.4 3 4c0-.6.4-1 1-1h3.5c.6 0 1 .4 1 1 0 1.3.2 2.5.6 3.6.1.3 0 .7-.2 1z"/></svg>
      (555) 740-1938
    </div>
    <div class="register">REGISTER AT: <span>WWW.C-SFPW.ORG/EVENTS</span></div>
  </footer>
</div>
</body>
</html>
```